We need a designer to help us represent our unique approach to creating lesson plans for digital learning. At the Autumn Gathering for Online Fluency, held in Providence RI this July 13 - 18, we'll use your design with 100 teachers and then put it online to reach hundreds of thousands more.

We have a draft visual of our model that we like - but it's not pretty (Since we are not designers, it looks a little clunky).

Please create a simple and attractive design in two versions: (1) one that we can use as a 1-page printed handout and (2) one that we can use where teachers can fill in sections and write ideas under each section of the graphic.

Why you should bid on this job? We're a leading provider of digital and media literacy curriculum resources with a huge international and national audience. Working with us will establish your expertise in the area of educational multimedia design.

Target Market(s)

Elementary and secondary teachers in public schools

Industry/Entity Type

Digital

Font styles to use
Sans Serif

Requirements
Must have
• TITLE : Digital Literacy Curriculum Framework

1 page version - suitable for use as a poster or 1-page flyer

Fillable form version - suitable for use as a handout with spaces for teachers to write

```html
<!DOCTYPE html>
<html lang="en">
<head>
<meta charset="utf-8">
<title>Digital Literacy Curriculum Framework</title>
<link rel="stylesheet" href="https://fonts.googleapis.com/css2?family=Cinzel:wght@500;600&family=Comic+Neue:ital,wght@0,700;1,700&display=swap">
<style>
  :root {
    --canvas: #ffffff;
    --band: rgba(105, 105, 105, 0.86);
    --title: #ffffff;
    --ink: #ffffff;
    --outline: #111111;
    --tone-pink: rgba(214, 70, 140, 0.75);
    --tone-olive: rgba(196, 170, 50, 0.7);
    --tone-green: rgba(45, 165, 90, 0.7);
    --tone-blue: rgba(45, 130, 210, 0.7);
    --tone-orange: rgba(224, 134, 42, 0.7);
    --glow-purple: #5a1a7a;
    --glow-red: #7a1a1a;
  }
  html, body {
    margin: 0;
    padding: 0;
    overflow: hidden;
    background: var(--canvas);
  }
  .framework {
    position: relative;
    width: 1200px;
    height: 1000px;
    overflow: hidden;
    background: var(--canvas);
    font-family: "Comic Neue", "Comic Sans MS", sans-serif;
    font-weight: 700;
  }
  .framework-artwork {
    position: absolute;
    left: 40px;
    top: 60px;
    width: 1120px;
    height: 940px;
    border-radius: 50%;
    background: linear-gradient(135deg,
      var(--tone-pink) 15%,
      var(--tone-olive) 40%,
      var(--tone-green) 55%,
      var(--tone-blue) 70%,
      var(--tone-orange) 90%);
    -webkit-mask-image: radial-gradient(ellipse at 50% 50%, #000 40%, transparent 70%);
    mask-image: radial-gradient(ellipse at 50% 50%, #000 40%, transparent 70%);
  }
  .title-band {
    position: absolute;
    left: 0;
    top: 0;
    width: 1200px;
    height: 140px;
    background: var(--band);
    display: flex;
    align-items: center;
    justify-content: center;
  }
  .title-band h1 {
    margin: 0;
    font-family: "Cinzel", "Trajan Pro", serif;
    font-weight: 600;
    font-size: 54px;
    line-height: 60px;
    letter-spacing: 2px;
    color: var(--title);
    text-align: center;
    text-shadow: 0 0 4px #000, 2px 2px 3px #000;
  }
  .label {
    position: absolute;
    margin: 0;
    color: var(--ink);
    line-height: 1.05;
    white-space: nowrap;
    text-shadow:
      -2px -2px 0 var(--outline), 2px -2px 0 var(--outline),
      -2px 2px 0 var(--outline), 2px 2px 0 var(--outline),
      0 0 6px rgba(0,0,0,0.6);
  }
  .label--corner {
    font-style: italic;
    font-size: 56px;
    text-shadow:
      -1.5px -1.5px 0 var(--outline), 1.5px -1.5px 0 var(--outline),
      -1.5px 1.5px 0 var(--outline), 1.5px 1.5px 0 var(--outline);
  }
  .corner-purpose { left: 12px; top: 150px; }
  .corner-assessment { right: 6px; top: 134px; }
  .corner-content { left: 10px; top: 828px; }
  .corner-pedagogy { right: 18px; top: 830px; }

  .element-standards {
    left: 215px; top: 240px; font-size: 70px;
    text-shadow: -2px -2px 0 var(--glow-purple), 2px -2px 0 var(--glow-purple),
      -2px 2px 0 var(--glow-purple), 2px 2px 0 var(--glow-purple), 0 0 8px var(--glow-purple);
  }
  .element-work-products { left: 790px; top: 220px; font-size: 48px; line-height: 52px; text-align: center; }
  .element-learners { left: 505px; top: 356px; font-size: 62px; }
  .element-task { left: 515px; top: 445px; font-size: 62px; text-align: center; width: 220px; }
  .element-context {
    left: 520px; top: 594px; font-size: 60px;
    text-shadow: -2px -2px 0 var(--glow-red), 2px -2px 0 var(--glow-red),
      -2px 2px 0 var(--glow-red), 2px 2px 0 var(--glow-red), 0 0 6px var(--glow-red);
  }
  .element-texts { left: 178px; top: 568px; font-size: 100px; }
  .element-tools {
    left: 525px; top: 778px; font-size: 100px;
    text-shadow: -3px -3px 0 var(--glow-red), 3px -3px 0 var(--glow-red),
      -3px 3px 0 var(--glow-red), 3px 3px 0 var(--glow-red), 0 0 8px #000;
  }
  .element-strategies { left: 836px; top: 550px; font-size: 50px; line-height: 54px; text-align: center; }
  .element-self {
    left: 418px; top: 552px; font-size: 48px;
    transform: rotate(-90deg); transform-origin: left top;
  }
  .element-community {
    left: 832px; top: 378px; font-size: 44px;
    transform: rotate(90deg); transform-origin: left top;
  }
</style>
</head>
<body>
<main class="framework">
  <div class="framework-artwork" role="img" aria-label="Large multicoloured flower with petals in pink, olive, green, blue and orange radiating from the centre"></div>

  <header class="title-band">
    <h1>Digital Literacy Curriculum<br>Framework</h1>
  </header>

  <p class="label label--corner corner-purpose">Purpose</p>
  <p class="label label--corner corner-assessment">Assessment</p>
  <p class="label label--corner corner-content">Content</p>
  <p class="label label--corner corner-pedagogy">Pedagogy</p>

  <p class="label element-standards">Standards</p>
  <p class="label element-work-products">Work<br>products</p>
  <p class="label element-learners">Learners</p>
  <p class="label element-task">Task or<br>activity</p>
  <p class="label element-context">Context</p>
  <p class="label element-texts">Texts</p>
  <p class="label element-tools">Tools</p>
  <p class="label element-strategies">Instructional<br>strategies</p>
  <p class="label element-self">Self</p>
  <p class="label element-community">Community</p>
</main>
</body>
</html>
```